www.tilbrookhealth.com

We are a company that is in the business of extending the life of surgical equipment by repairing or refurbishing equipment to save hospitals, surgery centers and clinics money. We call ourselves Tilbrook Medical Corporation. We are in need of a website that delivers the "feel" of what of we do everyday. A website that explains our services but at the same time has a touch that is different from the rest. Many companies repair but their websites may not "pull" customers to inquire, we need that punch. At this time we are not looking for e-commerce but would like the option of adding that in the future. We do sell new and used equipment, so we like to be able to highlight those manufacturers on our site. We would like the website to have enough layouts for pictures to describe what we repair.
Target Market(s)
Biomedical Technicians and Managers, Hospital Purchasing Departments, OR Managers, type of facilities that our customer exists in, hospitals, surgery centers, clinics, animal hospitals
Industry/Entity Type
E-Commerce
Requirements
Must have
- An easy to navigate website, modern looking.
Easy to modify with pictures and or additional web pages
The winning designer to be available for future modifications and changes
Website to be unique compared to our competition, which are numerous
Nice to have
- E-Commerce capability

```html
<!DOCTYPE html>
<html lang="en">
<head>
<meta charset="utf-8">
<title>Tilbrook Medical Corporation</title>
<link rel="stylesheet" href="https://fonts.googleapis.com/css2?family=Source+Sans+3:wght@300;400;600&family=PT+Sans+Narrow:wght@400;700&display=swap">
<style>
:root{
  --page-bg:#eef0f2;
  --white:#ffffff;
  --blue:#1f5fb5;
  --blue-text:#2a66b8;
  --green:#4aa531;
  --green-dark:#2f8a1e;
  --text:#555a60;
  --line:#dcdfe3;
  --footer:#2f3032;
  --footer-text:#e8e8e8;
}
*{box-sizing:border-box;margin:0;padding:0}
html,body{width:870px;height:1200px;overflow:hidden}
body{background:var(--page-bg);font-family:"Source Sans 3",sans-serif;color:var(--text);position:relative}
.page{position:absolute;left:58px;top:0;width:754px;height:1092px;background:var(--white);border-left:1px solid var(--line);border-right:1px solid var(--line)}
.abs{position:absolute}
.brand{left:26px;top:30px;display:flex;align-items:center;gap:8px;font-weight:600;font-size:26px;color:var(--green-dark);letter-spacing:.3px}
.brand-mark{width:22px;height:22px;border-radius:50%;background:var(--green)}
.top-links{right:24px;top:8px;font-size:9px;color:#666}
.top-links span{margin:0 3px;color:#999}
.cart{left:654px;top:30px;width:79px;height:27px;border-radius:3px;background:linear-gradient(#6cc04a,#3f9b26);color:#fff;font-size:13px;display:flex;align-items:center;justify-content:center;gap:5px}
.search{left:540px;top:65px;width:193px;height:25px;border:1px solid #d4d6d9;background:#fff;font-size:10px;font-style:italic;color:#999;padding:6px 9px}
.search svg{position:absolute;right:7px;top:5px}
.nav{left:0;top:104px;width:754px;height:38px;background:linear-gradient(#2d74c9,#1b5caf);display:flex}
.nav a{font-family:"PT Sans Narrow",sans-serif;color:#fff;text-decoration:none;font-size:14px;display:flex;align-items:center;justify-content:center;border-right:1px solid #4a86cf}
.nav a:last-child{border-right:none}
.hero{left:1px;top:142px;width:752px;height:282px;
  background:
    radial-gradient(ellipse 120px 70px at 22% 20%,rgba(90,120,150,.45),transparent 70%),
    radial-gradient(ellipse 90px 60px at 53% 38%,rgba(70,100,135,.4),transparent 70%),
    radial-gradient(ellipse 110px 80px at 86% 20%,rgba(40,55,70,.55),transparent 70%),
    radial-gradient(ellipse 170px 60px at 60% 85%,rgba(60,70,80,.45),transparent 70%),
    radial-gradient(ellipse 140px 110px at 38% 30%,rgba(255,255,255,.9),transparent 70%),
    linear-gradient(180deg,#aeb5bc 0%,#e4e7e9 25%,#f3f4f5 55%,#d6dadd 80%,#b9bec3 100%)}
.hero-ctrl{left:717px;top:395px;width:36px;height:29px;background:rgba(255,255,255,.85);display:flex;align-items:center;justify-content:center}
.card{top:442px;width:233px;height:200px;border:1px solid #dde0e3;background:linear-gradient(#fff 60%,#f2f3f4);overflow:hidden}
.card .ph{position:absolute;left:15px;top:13px;width:203px;height:87px;border:1px solid #d6d9dc}
.card h3{position:absolute;left:15px;top:107px;font-weight:400;font-size:16px;color:var(--green)}
.card p{position:absolute;left:15px;top:132px;width:210px;font-size:10px;font-weight:300;line-height:17px;color:#777}
.card .more{position:absolute;left:16px;top:168px;font-family:"PT Sans Narrow",sans-serif;font-size:11.5px;color:#333}
.card svg.swoosh{position:absolute;right:0;bottom:0}
.welcome h1{font-weight:300;font-size:20px;color:#333;letter-spacing:-.2px}
.welcome p{margin-top:7px;font-size:9.6px;font-weight:300;line-height:18.4px;color:#444}
.latest{left:24px;top:818px;font-family:"PT Sans Narrow",sans-serif;font-size:16px;color:var(--blue-text);font-weight:700}
.product{top:846px;width:107px}
.product .ph{height:96px;border:1px solid #e3e5e8}
.product h4{margin-top:9px;font-weight:400;font-size:12px;color:var(--blue-text)}
.product p{font-size:9px;font-weight:300;line-height:13px;color:#777;margin-top:2px}
.product .btn{margin-top:6px;width:53px;height:19px;background:linear-gradient(#5fb541,#3d951f);color:#fff;font-size:8px;font-weight:600;display:flex;align-items:center;justify-content:center;border-radius:2px}
.divider{left:503px;top:672px;width:1px;height:376px;background:#e2e4e7}
.side h2{font-weight:400;font-size:19px}
.side-how{left:527px;top:660px;width:206px}
.side-how h2{color:var(--blue-text)}
.side-how .ph{margin-top:5px;height:87px;border:1px solid #ddd}
.side-how .lead{margin-top:8px;font-size:13px;font-weight:300;color:#333}
.side-how p{margin-top:3px;font-size:9.5px;font-weight:300;line-height:18px;color:#555}
.side-services{left:527px;top:862px;width:206px}
.side-services h2{color:var(--green)}
.side-services ul{list-style:none;margin-top:5px}
.side-services li{height:23.5px;border-bottom:1px solid #e6e8ea;font-size:10px;color:#333;display:flex;align-items:center;padding-left:17px;position:relative}
.side-services li:last-child{border-bottom:none}
.side-services li::before{content:"";position:absolute;left:6px;top:8px;border-left:4px solid #999;border-top:4px solid transparent;border-bottom:4px solid transparent}
.footer{left:0;top:1092px;width:870px;height:108px;background:var(--footer)}
.footer-nav{left:78px;top:22px;font-family:"PT Sans Narrow",sans-serif;font-size:12px;color:var(--footer-text)}
.footer-nav span{margin:0 4px}
.copyright{left:78px;top:46px;font-size:9px;font-weight:300;color:#bbb}
.social{left:698px;top:20px;display:flex;gap:6px}
.social i{width:20px;height:20px;border-radius:3px;display:block}
</style>
</head>
<body>
<div class="page">
  <div class="abs brand"><span class="brand-mark"></span>Tilbrook Medical</div>
  <div class="abs top-links">My Account<span>|</span>Free Shipping<span>|</span>Customer Support</div>
  <div class="abs cart">
    <svg width="17" height="14" viewBox="0 0 17 14"><path d="M1 2h3l2 7h8l2-5H5" fill="none" stroke="#fff" stroke-width="1.5"/><circle cx="7" cy="12" r="1.3" fill="#fff"/><circle cx="13" cy="12" r="1.3" fill="#fff"/></svg>0 items</div>
  <div class="abs search">Search here..
    <svg width="14" height="14" viewBox="0 0 14 14"><circle cx="6" cy="6" r="4.3" fill="none" stroke="#666" stroke-width="2"/><path d="M9 9l4 4" stroke="#666" stroke-width="2.2"/></svg></div>

  <nav class="abs nav">
    <a style="width:75px">HOME</a><a style="width:82px">ABOUT US</a><a style="width:76px">SERVICES</a><a style="width:82px">REPARING</a><a style="width:84px">PRODUCTS</a><a style="width:80px">BUY NOW</a><a style="width:77px">SUPPORT</a><a style="width:106px">TESTIMONIALS</a><a style="width:92px">CONTACT</a>
  </nav>

  <div class="abs hero" role="img" aria-label="Hybrid operating room filled with surgical lights, monitors and imaging equipment"></div>
  <div class="abs hero-ctrl">
    <svg width="20" height="14" viewBox="0 0 20 14"><path d="M7 2L2 7l5 5M13 2l5 5-5 5" fill="none" stroke="#333" stroke-width="1.5"/></svg>
  </div>

  <div class="abs card" style="left:14px">
    <div class="ph" role="img" aria-label="Operating room with C-arm and monitors" style="background:radial-gradient(ellipse 40px 28px at 80% 55%,rgba(70,140,190,.8),transparent 70%),radial-gradient(ellipse 60px 40px at 45% 50%,rgba(245,245,240,.95),transparent 70%),linear-gradient(90deg,#9a7a5c,#c8b8a2 35%,#d8d8d2 60%,#4f6577 85%,#7c8e9a)"></div>
    <h3>Sell Medical Equipments</h3>
    <p>Proin nulla arcu nonummy luctus dictum eget, fermentum et lorem Nunc porta convallis</p>
    <div class="more">LEARN MORE &#9656;</div>
    <svg class="swoosh" width="110" height="22" viewBox="0 0 110 22"><path d="M0 22C40 20 80 12 110 0V22Z" fill="var(--blue)"/></svg>
  </div>
  <div class="abs card" style="left:262px">
    <div class="ph" role="img" aria-label="Technician repairing equipment at a workbench" style="background:radial-gradient(ellipse 45px 45px at 78% 65%,rgba(25,35,70,.9),transparent 75%),radial-gradient(ellipse 40px 30px at 22% 55%,rgba(250,250,250,.95),transparent 70%),linear-gradient(180deg,#c9cccf,#a9adb1 50%,#d9dcde)"></div>
    <h3>Reparing Medical Equipments</h3>
    <p>Proin nulla arcu nonummy luctus dictum eget, fermentum et lorem Nunc porta convallis</p>
    <div class="more">LEARN MORE &#9656;</div>
    <svg class="swoosh" width="110" height="22" viewBox="0 0 110 22"><path d="M0 22C40 20 80 12 110 0V22Z" fill="var(--blue)"/></svg>
  </div>
  <div class="abs card" style="left:509px">
    <div class="ph" role="img" aria-label="Lab staff working at microscopes" style="background:radial-gradient(ellipse 45px 40px at 35% 65%,rgba(255,255,255,.95),transparent 70%),radial-gradient(ellipse 50px 40px at 78% 70%,rgba(255,255,255,.95),transparent 70%),linear-gradient(180deg,#3e4d63 0%,#7d8794 35%,#cfd3d8 70%,#e9ebee)"></div>
    <h3>Refurbishing Equipment</h3>
    <p>Proin nulla arcu nonummy luctus dictum eget, fermentum et lorem Nunc porta convallis</p>
    <div class="more">LEARN MORE &#9656;</div>
    <svg class="swoosh" width="110" height="22" viewBox="0 0 110 22"><path d="M0 22C40 20 80 12 110 0V22Z" fill="var(--blue)"/></svg>
  </div>

  <section class="abs welcome" style="left:26px;top:674px;width:465px">
    <h1>WELCOME TO OUR WEBSITE MAINPAGE..</h1>
    <p>Phasellus felis dolor, scelerisque a, tempus eget, lobortis id, libero. Donec scelerisque leo ac risus. Praesent sit amet est. In dictum, dolor eu dictum porttitor, enim felis viverra mi, eget luctus massa purus q+uis odio. Etiam nulla massa, pharetra facilisis, volutpat in, imperdiet sit amet, sem.<br>Aliquam nec erat at purus cursus interdum. Vestibulum ligula augue, bibendum accumsan, vestibulum ut, commodo a, mi. Morbi ornare gravida elit. Integer congue, augue et malesuada iaculis</p>
  </section>

  <div class="abs latest">LATEST PRODUCTS</div>
  <div class="abs product" style="left:24px"><div class="ph" role="img" aria-label="Mobile C-arm imaging unit" style="background:radial-gradient(ellipse 35px 40px at 45% 55%,rgba(180,188,200,.8),transparent 70%),radial-gradient(ellipse 18px 40px at 85% 45%,rgba(150,160,175,.7),transparent 70%),#fafbfc"></div><h4>Product Name</h4><p>Vestibulum ligula augue, bibendum accumsan</p><div class="btn">DETAILS</div></div>
  <div class="abs product" style="left:142px"><div class="ph" role="img" aria-label="Surgical microscope" style="background:radial-gradient(ellipse 30px 30px at 55% 55%,rgba(40,42,48,.85),transparent 70%),radial-gradient(ellipse 30px 20px at 25% 20%,rgba(140,150,160,.7),transparent 70%),linear-gradient(#d3d7db,#f4f5f6)"></div><h4>Product Name</h4><p>Vestibulum ligula augue, bibendum accumsan</p><div class="btn">DETAILS</div></div>
  <div class="abs product" style="left:259px"><div class="ph" role="img" aria-label="Benchtop sterilizer unit" style="background:radial-gradient(ellipse 55px 35px at 50% 70%,rgba(245,245,243,1),transparent 70%),linear-gradient(#6f7c88,#aab3bb 40%,#d5d9dc)"></div><h4>Product Name</h4><p>Vestibulum ligula augue, bibendum accumsan</p><div class="btn">DETAILS</div></div>
  <div class="abs product" style="left:377px"><div class="ph" role="img" aria-label="Portable ultrasound system" style="background:radial-gradient(ellipse 25px 22px at 50% 30%,rgba(30,32,36,.9),transparent 75%),radial-gradient(ellipse 45px 25px at 48% 75%,rgba(200,205,212,.9),transparent 70%),#fafbfc"></div><h4>Product Name</h4><p>Vestibulum ligula augue, bibendum accumsan</p><div class="btn">DETAILS</div></div>

  <div class="abs divider"></div>

  <aside class="abs side side-how">
    <h2>How we Reparing</h2>
    <div class="ph" role="img" aria-label="Technician servicing a piece of medical equipment" style="background:radial-gradient(ellipse 50px 45px at 25% 55%,rgba(120,125,132,.8),transparent 70%),radial-gradient(ellipse 60px 30px at 75% 70%,rgba(235,232,220,1),transparent 70%),linear-gradient(90deg,#a8adb2,#dcdedf 55%,#f1f0ec)"></div>
    <div class="lead">Phasellus felis dolor scelerisque</div>
    <p>a, tempus eget, lobortis id, libero. Donec sceleris-que leo ac risus Praesent sit amet est.</p>
  </aside>
  <aside class="abs side side-services">
    <h2>Services Provide</h2>
    <ul>
      <li>Class aptent taciti sociosqu ad litora</li>
      <li>Torquent per conubia nostra</li>
      <li>Per inceptos hymenaeos</li>
      <li>Proin nulla arcu nonummy luctus</li>
      <li>Dictum eget fermentum et lorem</li>
    </ul>
  </aside>
</div>

<footer class="abs footer">
  <div class="abs footer-nav">HOME<span>|</span>ABOUT US<span>|</span>SERVICES<span>|</span>REPARING<span>|</span>PRODUCTS<span>|</span>BUY NOW<span>|</span>SUPPORT<span>|</span>TESTIMONIALS<span>|</span>CONTACT</div>
  <div class="abs copyright">Copyright &copy; 2013 Company Name. All rights reserved.</div>
  <div class="abs social" aria-label="Social links">
    <i style="background:#3b5a9a"></i><i style="background:#3aa3dc"></i><i style="background:#1b74b0"></i><i style="background:#e8842a"></i>
  </div>
</footer>
</body>
</html>
```